Media and Film Company Needs a New Website

We produce highly stylized commercials and film pieces for our clients. We also produce live events, both corporate and theatrical. Looking for a site that can show off our client videos - have a polished way to show off our team, and be able to create pages to highlight our clients and give a full overview of our project/process with them. We design simple website for some of our clients - so we are very wordpress familiar, and would like something that doesn't feel like a template.

Target Market(s)

content creators, creative directors, production teams, marketing agencies

Industry/Entity Type

Film Production

Number of Pages Required

4 page

Font styles to use
Sans Serif

Requirements
Must have
• slick looking video embed (from YT or Vimeo)
• project pages - client snapshot (what we did for them, how we did it)
• nice landing page, have our company video reel on the page
• testimonials
• contact page
• ability to have photos as a background if we want
Nice to have
• polished clean look - look to our logo colors and linear elements
• we produce very stylized videos for our clients and our website should reflect that
Should not have
• template look or feel to it- please bring your flare to the project!
• take a look at our current site - zantorvo.com we need a better way to highlight our work and our clients

```html
<!DOCTYPE html>
<html lang="en">
<head>
<meta charset="utf-8">
<title>Kestrel Media &amp; Entertainment</title>
<link rel="stylesheet" href="https://fonts.googleapis.com/css2?family=Raleway:ital,wght@0,300;0,400;0,500;0,600;0,700;0,800;1,400&display=swap">
<style>
:root{
  --yellow:#f2c11c;
  --magenta:#e0147b;
  --blue:#2b8bd0;
  --black:#111111;
  --ink:#333333;
  --muted:#8a8a8a;
  --white:#ffffff;
  --rule:#d9d9d9;
}
*{box-sizing:border-box;margin:0;padding:0}
html,body{width:1200px;height:4675px;overflow:hidden}
body{position:relative;background:var(--white);font-family:"Raleway",Arial,sans-serif;color:var(--ink)}
.abs{position:absolute}

/* header */
.site-header{left:0;top:0;width:1200px;height:131px;background:var(--white)}
.brand{left:40px;top:34px;display:flex;align-items:center;gap:12px}
.brand-mark{width:18px;height:18px;background:var(--magenta)}
.brand-name{font-weight:800;font-size:40px;letter-spacing:1px;color:var(--black);line-height:1}
.brand-sub{left:70px;top:80px;font-size:14px;font-weight:600;color:var(--black);letter-spacing:1px}
.main-nav{left:478px;top:48px;display:flex;gap:32px;font-size:17px;font-weight:500;color:var(--muted);letter-spacing:.5px}
.main-nav .active{color:var(--black);position:relative}
.main-nav .active::after{content:"";position:absolute;left:-4px;right:-4px;top:34px;height:3px;background:var(--yellow)}

/* hero */
.hero{left:0;top:131px;width:1200px;height:539px;background:var(--black)}
.hero-reel{left:31px;top:0;width:795px;height:539px;background:var(--yellow)}
.reel-label{left:285px;top:212px;color:var(--white);font-size:36px;letter-spacing:8px;font-weight:500;line-height:1.3}
.service-tiles{left:838px;top:0;width:324px;height:539px;display:flex;flex-direction:column;gap:10px}
.service-tile{height:127px;display:flex;align-items:center;gap:22px;padding-left:24px;color:var(--white);font-weight:800;font-size:18px;letter-spacing:1.5px;line-height:1.25;text-transform:uppercase}
.tile-black{background:var(--black);border:2px solid #333}
.tile-magenta{background:var(--magenta)}
.tile-yellow{background:var(--yellow)}
.tile-blue{background:var(--blue)}

/* intro */
.intro-title{left:0;top:728px;width:1200px;text-align:center;font-size:38px;font-weight:400;letter-spacing:6px;color:var(--black);line-height:52px}
.intro-lead{left:92px;top:866px;width:1020px;font-size:24px;line-height:39px;color:var(--ink);font-weight:400}
.intro-col{top:1040px;width:500px;font-size:15.5px;line-height:26px;color:var(--muted);font-weight:400}
.btn{background:var(--yellow);color:var(--white);text-align:center;border-radius:30px;font-weight:500;letter-spacing:1px}
.btn-contact{left:461px;top:1218px;width:278px;height:48px;line-height:48px;font-size:20px}

/* media */
.media{left:0;top:1365px;width:1200px;height:625px;background:var(--blue)}
.tab-videos{left:0;top:0;width:432px;height:82px;display:flex;align-items:center;gap:22px;padding-left:78px;color:var(--white);font-size:38px;letter-spacing:6px}
.tab-photo{left:432px;top:0;width:768px;height:82px;background:var(--yellow);display:flex;align-items:center;gap:22px;padding-left:14px;color:var(--black);font-size:34px;letter-spacing:6px}
.thumb{width:321px;height:181px;border:3px solid var(--white)}
.thumb-play{position:absolute;left:50%;top:50%;width:52px;height:52px;margin:-26px 0 0 -26px;border-radius:50%;background:var(--white);opacity:.9}
.pager{left:498px;top:560px;display:flex;gap:16px}
.pager span{width:56px;height:56px;border-radius:50%;border:3px solid var(--white);color:var(--white);font-size:26px;font-weight:700;text-align:center;line-height:50px}
.pager .on{background:var(--white);color:var(--blue)}

/* press */
.press-heading{left:0;top:2080px;width:1200px;display:flex;justify-content:center;align-items:center;gap:22px;font-size:40px;letter-spacing:6px;color:var(--black)}
.feature-title{left:100px;top:2210px;width:580px;font-size:34px;line-height:42px;font-weight:400;color:var(--black);text-transform:uppercase}
.feature-meta{left:100px;top:2310px;font-size:14px;color:var(--muted)}
.feature-photo{left:100px;top:2353px;width:564px;height:259px}
.feature-caption{left:100px;top:2624px;width:570px;font-size:14px;line-height:22px;color:var(--muted)}
.btn-more{width:70px;height:22px;line-height:22px;font-size:11px;font-weight:700}
.press-divider{left:714px;top:2219px;width:4px;height:510px;background:var(--black)}
.press-item{left:748px;width:340px;height:110px}
.press-thumb{left:0;top:0;width:125px;height:94px}
.press-item-title{left:165px;top:2px;width:180px;font-size:14px;line-height:19px;color:var(--ink);text-transform:uppercase}
.press-item .btn-more{left:165px;top:84px}
.press-rule{left:748px;width:340px;height:3px;background:var(--black)}

/* testimonials */
.testimonials{left:0;top:2862px;width:1200px;height:520px;background:var(--magenta);overflow:hidden}
.testimonials-title{left:0;top:60px;width:1200px;text-align:center;color:var(--white);font-size:38px;letter-spacing:6px}
.testimonial-quote{left:62px;top:160px;width:1080px;text-align:center;color:var(--white);font-style:italic;font-size:23px;line-height:42px}
.testimonial-name{left:0;top:388px;width:1200px;text-align:center;color:var(--white);font-weight:700;font-size:24px}
.testimonial-role{left:0;top:424px;width:1200px;text-align:center;color:var(--white);font-size:24px}
.dots{left:540px;top:466px;display:flex;gap:14px}
.dots span{width:28px;height:28px;border-radius:50%;border:3px solid var(--white)}
.dots .on{background:var(--white)}

/* partners */
.partner{display:flex;align-items:center;gap:10px;font-weight:700;font-size:26px;color:var(--black);height:50px}
.partner i{display:block;width:18px;height:18px}

/* contact */
.contact{left:0;top:4083px;width:1200px;height:592px;background:var(--black);color:var(--white)}
.contact-title{left:0;top:28px;width:1200px;display:flex;justify-content:center;align-items:center;gap:20px;font-size:38px;letter-spacing:6px}
.form-label{left:134px;top:100px;font-size:18px}
.field{border:2px solid #777;width:312px;height:59px;color:#888;font-size:17px;padding:16px 18px}
.field-message{left:464px;top:150px;width:315px;height:215px}
.btn-submit{left:592px;top:384px;width:187px;height:24px;line-height:24px;font-size:13px}
.info-label{left:890px;font-size:18px}
.info-text{left:890px;font-size:15px;line-height:22px;color:#ccc}
.footer-rule{left:134px;top:452px;width:932px;height:2px;background:#777}
.socials{left:498px;top:506px;display:flex;gap:12px}
.socials span{width:18px;height:18px;background:var(--white)}
</style>
</head>
<body>

<header class="site-header abs">
  <div class="brand abs"><span class="brand-mark"></span><span class="brand-name">Kestrel Media</span></div>
  <div class="brand-sub abs">&amp; Entertainment</div>
  <nav class="main-nav abs">
    <span class="active">HOME</span><span>ABOUT</span><span>PORTFOLIO</span><span>PRESS</span><span>TESTIMONIALS</span><span>CONTACT</span>
  </nav>
</header>

<section class="hero abs">
  <div class="hero-reel abs">
    <svg class="abs" style="left:220px;top:80px" width="330" height="340" viewBox="0 0 330 340">
      <path d="M40 20 Q20 10 20 40 L20 300 Q20 330 45 318 L305 190 Q325 170 305 150 Z" fill="#111"/>
      <circle cx="130" cy="170" r="112" fill="none" stroke="#fff" stroke-width="3"/>
    </svg>
    <div class="reel-label abs">DEMO<br>REEL</div>
  </div>
  <div class="service-tiles abs">
    <div class="service-tile tile-black">
      <svg width="62" height="62" viewBox="0 0 62 62"><rect x="6" y="10" width="50" height="42" fill="#fff" transform="rotate(-15 31 31)"/><g fill="#111" transform="rotate(-15 31 31)"><rect x="10" y="14" width="6" height="6"/><rect x="22" y="14" width="6" height="6"/><rect x="34" y="14" width="6" height="6"/><rect x="46" y="14" width="6" height="6"/><rect x="10" y="42" width="6" height="6"/><rect x="22" y="42" width="6" height="6"/><rect x="34" y="42" width="6" height="6"/><rect x="46" y="42" width="6" height="6"/></g></svg>
      <span>Film &amp; Media<br>Production</span>
    </div>
    <div class="service-tile tile-magenta">
      <svg width="62" height="62" viewBox="0 0 62 62"><rect x="14" y="6" width="12" height="34" rx="6" fill="#fff"/><path d="M8 34 H48 V56 H8 Z" fill="#fff"/></svg>
      <span>Live<br>Production</span>
    </div>
    <div class="service-tile tile-yellow">
      <svg width="62" height="62" viewBox="0 0 62 62"><path d="M6 24 H18 L48 8 V54 L18 38 H6 Z" fill="#fff"/><rect x="14" y="38" width="8" height="16" fill="#fff"/></svg>
      <span>PR,<br>Marketing &amp;<br>Advertising</span>
    </div>
    <div class="service-tile tile-blue">
      <svg width="62" height="62" viewBox="0 0 62 62"><rect x="6" y="10" width="50" height="44" fill="none" stroke="#fff" stroke-width="4"/><rect x="6" y="10" width="50" height="10" fill="#fff"/><g fill="#fff"><rect x="13" y="26" width="7" height="7"/><rect x="27" y="26" width="7" height="7"/><rect x="41" y="26" width="7" height="7"/><rect x="13" y="39" width="7" height="7"/><rect x="27" y="39" width="7" height="7"/><rect x="41" y="39" width="7" height="7"/></g></svg>
      <span>Events</span>
    </div>
  </div>
</section>

<section class="intro">
  <h1 class="intro-title abs">THE CHAIR IS OPEN...<br>HOW CAN WE HELP YOU TELL YOUR STORY?</h1>
  <p class="intro-lead abs">Kestrel Media &amp; Entertainment provides full-service campaigns in film and media production, live entertainment &amp; theatrical production, marketing &amp; advertising, and event management in the DC metro area.</p>
  <p class="intro-col abs" style="left:92px">Founded in 2009, Kestrel Media &amp; Entertainment has built a reputation working for clients including the Northlight Film Guild, Vanta Leaders, Marlow Music, Riverbend Community Network, and Halden Events.</p>
  <p class="intro-col abs" style="left:608px">We work to build strong relationships with its clients through full-service campaigns in multiple industries. Through community outreach, Kestrel develops its campaigns thoroughly to provide the most successful services to its clients.</p>
  <div class="btn btn-contact abs">CONTACT US</div>
</section>

<section class="media abs">
  <div class="tab-videos abs">
    <svg width="46" height="50" viewBox="0 0 46 50"><path d="M4 4 L42 25 L4 46 Z" fill="#fff"/></svg>VIDEOS
  </div>
  <div class="tab-photo abs">
    <svg width="52" height="52" viewBox="0 0 52 52"><circle cx="26" cy="26" r="24" fill="#111"/><circle cx="26" cy="26" r="10" fill="#f2c11c"/><circle cx="26" cy="26" r="5" fill="#111"/></svg>PHOTOGRAPHY
  </div>
  <div class="thumb abs" style="left:78px;top:125px;background:linear-gradient(135deg,#3b3f5c,#8a6a7a)" role="img" aria-label="Video still of an event venue title card"><span class="thumb-play"></span></div>
  <div class="thumb abs" style="left:430px;top:125px;background:linear-gradient(135deg,#c89a3a,#6a4b2e)" role="img" aria-label="Video still of a gala banner wall"><span class="thumb-play"></span></div>
  <div class="thumb abs" style="left:782px;top:125px;background:linear-gradient(180deg,#9fc4e4,#6f8f5a)" role="img" aria-label="Video still of a community center building"><span class="thumb-play"></span></div>
  <div class="thumb abs" style="left:78px;top:340px;background:linear-gradient(135deg,#e8cf9a,#b07a3e)" role="img" aria-label="Video still of an interview subject"><span class="thumb-play"></span></div>
  <div class="thumb abs" style="left:430px;top:340px;background:linear-gradient(135deg,#d7a36a,#7a4e2a)" role="img" aria-label="Video still of a performer on stage"><span class="thumb-play"></span></div>
  <div class="thumb abs" style="left:782px;top:340px;background:linear-gradient(180deg,#8fb46a,#4f7a3a)" role="img" aria-label="Video still of a speaker outdoors"><span class="thumb-play"></span></div>
  <div class="pager abs"><span class="on">1</span><span>2</span><span>3</span></div>
</section>

<section class="press">
  <h2 class="press-heading abs">
    <svg width="56" height="52" viewBox="0 0 56 52"><rect x="10" y="2" width="44" height="48" fill="#f2c11c"/><rect x="2" y="14" width="12" height="36" fill="#f2c11c"/><g fill="#fff"><rect x="18" y="10" width="28" height="4"/><rect x="18" y="20" width="28" height="4"/><rect x="18" y="30" width="28" height="4"/></g></svg>
    PRESS
  </h2>
  <h3 class="feature-title abs">Photo featured on Capital Stage Review – 10/13/13</h3>
  <p class="feature-meta abs">Posted in Photos in Print October 13, 2013 by Kestrel Media 0 Comments</p>
  <div class="feature-photo abs" style="background:linear-gradient(90deg,#2a2a2a,#5a5048 50%,#2a2a2a)" role="img" aria-label="Photo of two performers seated in conversation on stage"></div>
  <p class="feature-caption abs">Kestrel photographer Owen Brisco was featured in this Capital Stage Review article – Stage Veteran Lena Marsh Helps Educate Aspiring Young Artists – October 13, 2013 PDF of the Article</p>
  <div class="btn btn-more abs" style="left:100px;top:2710px">MORE</div>
  <div class="press-divider abs"></div>

  <div class="press-item abs" style="top:2219px">
    <div class="press-thumb abs" style="background:linear-gradient(135deg,#3a3a3a,#7a6a5a)" role="img" aria-label="Photo of a speaker at a podium"></div>
    <div class="press-item-title abs">Photo featured in Hospitality Trade Online – 9/27/13</div>
    <div class="btn btn-more abs">MORE</div>
  </div>
  <div class="press-rule abs" style="top:2335px"></div>
  <div class="press-item abs" style="top:2347px">
    <div class="press-thumb abs" style="background:linear-gradient(135deg,#151515,#4a3a3a)" role="img" aria-label="Photo of a presenter on a dark stage"></div>
    <div class="press-item-title abs">Photo featured in Hospitality Trade Online – 9/24/13</div>
    <div class="btn btn-more abs">MORE</div>
  </div>
  <div class="press-rule abs" style="top:2465px"></div>
  <div class="press-item abs" style="top:2478px">
    <div class="press-thumb abs" style="background:linear-gradient(135deg,#6a6a6a,#b8b0a0)" role="img" aria-label="Photo of a film crew with camera"></div>
    <div class="press-item-title abs">Ashford's Brisco brings Kestrel to Alderbrook</div>
    <div class="btn btn-more abs">MORE</div>
  </div>
  <div class="press-rule abs" style="top:2605px"></div>
  <div class="press-item abs" style="top:2628px">
    <div class="press-thumb abs" style="background:linear-gradient(135deg,#1a1a1a,#3d4a55)" role="img" aria-label="Photo of a screening room"></div>
    <div class="press-item-title abs">Our photo in the Capital Ledger – 6/21/12</div>
    <div class="btn btn-more abs">MORE</div>
  </div>
</section>

<section class="testimonials abs">
  <svg class="abs" style="left:62px;top:0" width="230" height="140" viewBox="0 0 230 140"><rect x="0" y="0" width="92" height="140" fill="#fff"/><rect x="128" y="0" width="92" height="140" fill="#fff"/></svg>
  <svg class="abs" style="left:945px;top:400px" width="230" height="140" viewBox="0 0 230 140"><rect x="0" y="0" width="92" height="120" fill="#fff"/><rect x="128" y="0" width="92" height="120" fill="#fff"/></svg>
  <h2 class="testimonials-title abs">TESTIMONIALS</h2>
  <p class="testimonial-quote abs">Thank you very much for all the hard work and creativity that you devoted to the RCN video, which was moving and uplifting and captured the essence of what we try to do so very well. It made a strong and very positive impact on the guests at the dinner, and elicited many very favorable comments. I am grateful to you for the very significant contribution that you made to the success of our 18th annual Marian Holloway Benefit, and for all your help to RCN</p>
  <p class="testimonial-name abs">Daniel Whitcomb</p>
  <p class="testimonial-role abs">Executive Director, Riverbend Community Network.</p>
  <div class="dots abs"><span class="on"></span><span></span><span></span></div>
</section>

<section class="partners">
  <div class="partner abs" style="left:190px;top:3520px"><i style="background:#1f3a6b"></i>Vanta Leaders</div>
  <div class="partner abs" style="left:512px;top:3520px">Prism Provisions</div>
  <div class="partner abs" style="left:810px;top:3520px;color:#e07a1a">Corporal's</div>
  <div class="partner abs" style="left:185px;top:3610px;color:#1f3a6b">RCN</div>
  <div class="partner abs" style="left:490px;top:3610px;font-size:20px"><i style="background:#c0182a;border-radius:50%"></i>Civic Records Trust</div>
  <div class="partner abs" style="left:810px;top:3610px">Tabletech</div>
  <div class="partner abs" style="left:185px;top:3706px;font-size:22px;letter-spacing:2px">SECOND FRAME</div>
  <div class="partner abs" style="left:548px;top:3706px;color:#c0182a">Marlow Music</div>
  <div class="partner abs" style="left:785px;top:3706px;color:#e07a1a"><i style="background:#e07a1a;border-radius:50%"></i>Orbit Fest</div>
  <div class="partner abs" style="left:200px;top:3820px">Verity Docs</div>
  <div class="partner abs" style="left:522px;top:3820px;font-size:30px">HARLOW</div>
  <div class="partner abs" style="left:790px;top:3820px;font-size:22px">Treeline Filmworks</div>
  <div class="partner abs" style="left:175px;top:3912px;color:#2e8b57;font-size:22px">Well Paths</div>
  <div class="partner abs" style="left:470px;top:3912px"><i style="background:#111;border-radius:50%"></i>Small Motor</div>
  <div class="partner abs" style="left:795px;top:3912px"><i style="background:#c0182a;border-radius:50%"></i>Brightview</div>
</section>

<footer class="contact abs">
  <h2 class="contact-title abs">
    <svg width="46" height="46" viewBox="0 0 46 46"><path d="M4 8 L16 4 L30 10 L42 6 V38 L30 42 L16 36 L4 40 Z" fill="none" stroke="#f2c11c" stroke-width="4" stroke-linejoin="round"/><path d="M16 4 V36 M30 10 V42" stroke="#f2c11c" stroke-width="4"/></svg>
    CONTACT US
  </h2>
  <p class="form-label abs">Leave a message</p>
  <div class="field abs" style="left:134px;top:150px">name</div>
  <div class="field abs" style="left:134px;top:231px">email</div>
  <div class="field abs" style="left:134px;top:306px">phone</div>
  <div class="field field-message abs">message</div>
  <div class="btn btn-submit abs">SUBMIT</div>

  <svg class="abs" style="left:848px;top:100px" width="22" height="28" viewBox="0 0 22 28"><path d="M11 0 C4 0 0 5 0 11 C0 18 11 28 11 28 C11 28 22 18 22 11 C22 5 18 0 11 0 Z" fill="#fff"/><circle cx="11" cy="11" r="4" fill="#111"/></svg>
  <p class="info-label abs" style="top:102px">Location</p>
  <p class="info-text abs" style="top:130px">Kestrel Media &amp; Entertainment<br>4410 Meadow Lane #210<br>Alderbrook, MD 20990</p>
  <svg class="abs" style="left:848px;top:222px" width="24" height="18" viewBox="0 0 24 18"><rect width="24" height="18" fill="#fff"/><path d="M0 0 L12 10 L24 0" fill="none" stroke="#111" stroke-width="2"/></svg>
  <p class="info-label abs" style="top:218px">Email</p>
  <p class="info-text abs" style="top:248px">info@zantorvo.com</p>
  <svg class="abs" style="left:850px;top:310px" width="20" height="22" viewBox="0 0 20 22"><path d="M4 0 L8 6 L5 9 C7 13 9 15 12 17 L15 14 L20 18 L17 22 C8 20 2 13 0 4 Z" fill="#fff"/></svg>
  <p class="info-label abs" style="top:310px">Telephone</p>
  <p class="info-text abs" style="top:340px">+1 240 555 0142</p>

  <div class="footer-rule abs"></div>
  <div class="socials abs"><span></span><span></span><span></span><span></span><span></span><span></span></div>
</footer>

</body>
</html>
```